Lumo4Kart - a fintech company - business card

We need a business card design for our Payments Technology company in Sydney, Australia. We provide business with payment solutions expanding across EFTPOS machines, online payment gateways and mobile payment solutions. We would like to see designs that are clean, classy and professional.
Target Market(s)
Business professionals, executives, c-suite
Industry/Entity Type
Fintech
Contact Information for Business Card
Will be on 400gsm. Logo will most likely be spot gloss unless designer recommends otherwise.
Font styles to use
Sans Serif
Requirements
Must have
- We need our website (lumo4kart.com.au), email (contact@lumo4kart.com.au), mobile (0432 587 904) and direct phone number (02 6815 3927) to feature on the card along with our logo (attached) and the words "EFTPOS | ONLINE | MOBILE"
- Font = Roboto

```html
<!DOCTYPE html>
<html lang="en">
<head>
<meta charset="utf-8">
<title>Lumo4Kart – Business Card</title>
<link rel="stylesheet" href="https://fonts.googleapis.com/css2?family=Roboto:wght@400;700;900&family=Roboto+Condensed:wght@700&display=swap">
<style>
  :root {
    --brand-blue: #1a67a3;
    --brand-blue-deep: #145a90;
    --brand-blue-light: #2a7dbd;
    --tagline-blue: #17609a;
    --logo-grey: #5e6062;
    --divider-grey: #8a8c8e;
    --card-white: #f7f7f7;
    --card-shade: #e6e6e6;
    --backdrop: #2b2b2b;
    --contact-white: #ffffff;
  }

  * { box-sizing: border-box; margin: 0; padding: 0; }

  html, body {
    width: 1200px;
    height: 900px;
    overflow: hidden;
  }

  body {
    background: var(--backdrop);
    font-family: "Roboto", Arial, sans-serif;
    display: flex;
    flex-direction: column;
    align-items: center;
    justify-content: center;
    gap: 40px;
  }

  .card {
    position: relative;
    width: 620px;
    height: 380px;
    overflow: hidden;
    background: radial-gradient(circle at 30% 60%, var(--card-white) 0%, var(--card-shade) 100%);
    box-shadow: 0 14px 30px rgba(0, 0, 0, 0.55);
  }

  /* Shared wordmark */
  .wordmark {
    position: absolute;
    display: flex;
    align-items: center;
    gap: 12px;
    white-space: nowrap;
  }
  .wordmark__dot {
    width: 28px;
    height: 28px;
    border-radius: 50%;
    background: var(--brand-blue);
    flex: none;
  }
  .wordmark__name {
    font-family: "Roboto", Arial, sans-serif;
    font-weight: 900;
    font-size: 36px;
    line-height: 1;
    color: var(--logo-grey);
    letter-spacing: 0.5px;
    text-transform: uppercase;
  }

  /* Contact side */
  .card--contact .contact-arc {
    position: absolute;
    left: 250px;
    top: -340px;
    width: 580px;
    height: 580px;
    border-radius: 50%;
    background: linear-gradient(160deg, var(--brand-blue-light) 0%, var(--brand-blue-deep) 100%);
    box-shadow: -4px 6px 10px rgba(0, 0, 0, 0.25);
  }
  .card--contact .wordmark {
    left: 56px;
    top: 266px;
  }

  .contact-list {
    position: absolute;
    left: 380px;
    top: 58px;
    list-style: none;
    display: flex;
    flex-direction: column;
    gap: 9px;
  }
  .contact-list__item {
    display: flex;
    align-items: center;
    gap: 12px;
    color: var(--contact-white);
    font-size: 15px;
    font-weight: 400;
    white-space: nowrap;
  }
  .contact-list__icon {
    width: 16px;
    height: 16px;
    flex: none;
  }

  /* Front side */
  .card--front .feature-circle {
    position: absolute;
    left: 330px;
    top: -130px;
    width: 440px;
    height: 440px;
    border-radius: 50%;
    background: radial-gradient(circle at 55% 35%, var(--brand-blue-light) 0%, var(--brand-blue) 55%, var(--brand-blue-deep) 100%);
    box-shadow: -6px 8px 14px rgba(0, 0, 0, 0.25);
  }
  .card--front .wordmark {
    left: 50px;
    top: 122px;
  }

  .service-line {
    position: absolute;
    left: 52px;
    bottom: 44px;
    display: flex;
    align-items: center;
    font-family: "Roboto Condensed", "Roboto", Arial, sans-serif;
    font-weight: 700;
    font-size: 19px;
    color: var(--tagline-blue);
    letter-spacing: 0.3px;
  }
  .service-line__divider {
    width: 1px;
    height: 20px;
    background: var(--divider-grey);
    margin: 0 9px;
  }
</style>
</head>
<body>

  <section class="card card--contact" aria-label="Card back with contact details">
    <div class="contact-arc"></div>

    <ul class="contact-list">
      <li class="contact-list__item">
        <svg class="contact-list__icon" viewBox="0 0 16 16" aria-hidden="true">
          <rect x="4" y="1" width="8" height="14" rx="1.5" fill="none" stroke="#fff" stroke-width="1.4"/>
          <line x1="7" y1="12.5" x2="9" y2="12.5" stroke="#fff" stroke-width="1.4"/>
        </svg>
        <span>0432 587 904</span>
      </li>
      <li class="contact-list__item">
        <svg class="contact-list__icon" viewBox="0 0 16 16" aria-hidden="true">
          <path d="M3.5 1.5 L6 4 L4.8 5.8 C5.6 7.8 8.2 10.4 10.2 11.2 L12 10 L14.5 12.5 L12.8 14.5 C7.5 14 2 8.5 1.5 3.2 Z" fill="#fff"/>
        </svg>
        <span>02 6815 3927</span>
      </li>
      <li class="contact-list__item">
        <svg class="contact-list__icon" viewBox="0 0 16 16" aria-hidden="true">
          <rect x="1.5" y="3.5" width="13" height="9" rx="1" fill="none" stroke="#fff" stroke-width="1.4"/>
          <polyline points="1.5,4 8,9 14.5,4" fill="none" stroke="#fff" stroke-width="1.4"/>
        </svg>
        <span>contact@lumo4kart.com.au</span>
      </li>
      <li class="contact-list__item">
        <svg class="contact-list__icon" viewBox="0 0 16 16" aria-hidden="true">
          <circle cx="8" cy="8" r="6.5" fill="none" stroke="#fff" stroke-width="1.3"/>
          <ellipse cx="8" cy="8" rx="3" ry="6.5" fill="none" stroke="#fff" stroke-width="1.1"/>
          <line x1="1.5" y1="8" x2="14.5" y2="8" stroke="#fff" stroke-width="1.1"/>
        </svg>
        <span>lumo4kart.com.au</span>
      </li>
    </ul>

    <div class="wordmark">
      <span class="wordmark__dot" aria-hidden="true"></span>
      <span class="wordmark__name">Lumo4Kart</span>
    </div>
  </section>

  <section class="card card--front" aria-label="Card front">
    <div class="feature-circle"></div>

    <div class="wordmark">
      <span class="wordmark__dot" aria-hidden="true"></span>
      <span class="wordmark__name">Lumo4Kart</span>
    </div>

    <p class="service-line">
      <span>EFTPOS</span>
      <span class="service-line__divider" aria-hidden="true"></span>
      <span>ONLINE</span>
      <span class="service-line__divider" aria-hidden="true"></span>
      <span>MOBILE</span>
    </p>
  </section>

</body>
</html>
```